The most modern business card ever !!!

Our company call “Vantilo”. Vantilo is a technology company specialized in cruises solutions. Out main product is a platform to reserve cruises. This is a revolutionary platform that make easier to travel agencies and final users to reserve cruises across dozen companies like tarvik, welbi, dpv, hbt, etc..We are a “start up”, with a young team of developers and we want to transmit it.. For it, we want something different, a modern business card that represent cruises and technology.. When someone receive this card, this person should say: wowww this is different… this is modern… this is a cruise related company..
Contact Information for Business Card
Requirements
Must have
- diferent, modern
Should not have
- traditions business card

```html
<!DOCTYPE html>
<html lang="en">
<head>
<meta charset="utf-8">
<title>Vantilo Business Card</title>
<link href="https://fonts.googleapis.com/css2?family=Open+Sans:wght@400;600;700&display=swap" rel="stylesheet">
<style>
  :root {
    --bg: #e9ebee;
    --card-white: #ffffff;
    --brand-blue: #29a6df;
    --brand-blue-light: #45b4e6;
    --wave-deep: #5aa8d6;
    --wave-light: #cfe7f5;
    --ink: #1d1f22;
    --ink-soft: #45484d;
    --accent: #2a9fd8;
  }
  * { margin: 0; padding: 0; box-sizing: border-box; }
  html, body {
    width: 1200px; height: 1200px; overflow: hidden;
    background: var(--bg);
    font-family: "Open Sans", Arial, sans-serif;
  }
  .canvas {
    width: 1200px; height: 1200px;
    display: flex; flex-direction: column; align-items: center; justify-content: center;
    gap: 60px;
  }
  .card {
    position: relative;
    width: 800px; height: 457px;
    overflow: hidden;
    box-shadow: 0 6px 18px rgba(0,0,0,0.12);
  }
  .card-front { background: var(--card-white); }
  .card-back {
    background: linear-gradient(135deg, var(--brand-blue) 0%, var(--brand-blue-light) 100%);
    display: flex; align-items: center; justify-content: center;
  }

  .wave-band { position: absolute; left: 0; top: 0; width: 800px; height: 457px; }
  .ship-art {
    position: absolute; left: 70px; top: 150px; width: 170px; height: 110px;
    border-radius: 10px 40px 10px 10px;
    background: linear-gradient(160deg, #f4f6f8 0%, #c9d1d8 100%);
  }

  .holder { position: absolute; left: 60px; top: 52px; }
  .holder-name { font-size: 28px; font-weight: 600; color: var(--ink); }
  .holder-role { font-size: 15px; color: var(--accent); margin-top: 2px; }

  .wordmark {
    position: absolute; left: 420px; top: 110px;
    font-size: 66px; font-weight: 600; letter-spacing: 3px; color: var(--ink);
    line-height: 1;
  }
  .address {
    position: absolute; left: 430px; top: 205px;
    font-size: 16px; line-height: 24px; color: var(--ink-soft);
  }
  .contact {
    position: absolute; left: 430px; top: 270px;
    display: grid; grid-template-columns: 90px auto; row-gap: 4px;
    font-size: 16px; color: var(--ink-soft);
  }

  .back-wordmark {
    font-size: 120px; font-weight: 600; letter-spacing: 6px; color: var(--ink);
    line-height: 1;
  }
</style>
</head>
<body>
<main class="canvas">
  <section class="card card-front">
    <svg class="wave-band" viewBox="0 0 800 457" aria-hidden="true">
      <defs>
        <linearGradient id="sea" x1="0" y1="0" x2="0" y2="1">
          <stop offset="0" stop-color="var(--wave-light)"/>
          <stop offset="1" stop-color="var(--wave-deep)"/>
        </linearGradient>
      </defs>
      <path d="M0 235 C 120 225, 200 255, 300 295 C 420 345, 560 400, 800 440 L 800 457 L 0 457 Z" fill="url(#sea)"/>
      <path d="M0 300 C 140 290, 240 320, 340 360 C 440 398, 540 430, 640 457 L 0 457 Z" fill="var(--wave-deep)" opacity="0.45"/>
    </svg>
    <div class="ship-art" role="img" aria-label="Illustration of a white cruise ship sailing on the waves"></div>

    <div class="holder">
      <div class="holder-name">Marco Linde</div>
      <div class="holder-role">Director</div>
    </div>

    <div class="wordmark">Vantilo</div>

    <div class="address">
      <div>Harbor city</div>
      <div>Marlow Country Land</div>
    </div>

    <div class="contact">
      <span>Phone</span><span>1-555-204817</span>
      <span>Web</span><span>www.vantilo.com</span>
      <span>Email</span><span>marco@vantilo.com</span>
    </div>
  </section>

  <section class="card card-back">
    <div class="back-wordmark">Vantilo</div>
  </section>
</main>
</body>
</html>
```